Oakvane Residential Flyer

Quarter-page leave-behind flyer for a commercial cleaning company (print)

ABOUT US
Trellow Commercial Cleaning is a Texas-owned commercial cleaning company serving Austin for over 20 years. We were recently named to Oakvane Residential's Capitol Partner Circle, a preferred vendor program covering apartment communities across the Austin metro. Our sales team will hand this flyer to apartment community managers during property visits.

THE JOB THIS FLYER MUST DO
A busy property manager should scan it in five seconds, understand what we do, trust us and keep the card on their desk. The call to action is booking a free walkthrough of their community. Do not include any pricing.

SPECS
Size: 4.25 x 5.5 inches (quarter of a letter page), single sided, portrait. Print ready with 0.125 inch bleed, CMYK, 300 dpi minimum. Vector preferred.

REQUIRED CONTENT
Headline: The clean your residents notice.
Badge or tagline: Oakvane Residential's Approved Austin Cleaning Company.
Supporting line: Preferred Vendor Partner in Oakvane's Capitol Partner Circle. Texas-owned, serving Austin for 20+ years.
Services (icons welcome): recurring janitorial, floor strip wax and buff, carpet extraction, windows and glass, upholstery care, pressure washing, move-in and move-out cleans, damage restoration.
Trust points: licensed and insured, background-checked crews, TrustGrid compliant, invoicing through Supply Nook and Kelvara Systems.

Social proof line: Already trusted by Oakvane communities. Ask your peers at The Brindley and The Ashford on Tulley.

Call to action: Book a free walkthrough of your community. Call or email 512-430-7156 or support@trellowclean-example.com

STYLE DIRECTION
Clean, crisp and premium. Whiteness and shine should feel like part of the message. We like a deep green and teal palette with one warm accent, but strong alternative directions are welcome. Custom icons over clip art.
AVOID
Stock photos of cleaners with buckets, cartoon mascots, sparkle overload, cluttered layouts, any prices or dollar amounts.
DELIVERABLES
Print-ready PDF with bleed and crop marks, plus editable source files (AI, PSD or Figma). A version with our logo placement marked, since we will supply the logo file to the winner.

```html
<!DOCTYPE html>
<html lang="en">
<head>
<meta charset="utf-8">
<title>Oakvane Residential Flyer – Trellow Commercial Cleaning</title>
<link rel="stylesheet" href="https://fonts.googleapis.com/css2?family=Merriweather:ital,wght@0,700;0,900;1,900&family=Open+Sans:ital,wght@0,400;0,600;0,700;1,300;1,600&family=Poppins:wght@400;500&display=swap">
<style>
  :root {
    --backdrop: #a4a8a6;
    --paper: #ffffff;
    --forest: #133b32;
    --teal: #1a9180;
    --gold: #e8a92a;
    --gold-soft: #f1c97a;
    --peach-line: #f2cdb8;
    --mint: #e8f3f1;
    --mint-panel: #eef6f5;
    --ink: #1d2a27;
  }
  * { box-sizing: border-box; margin: 0; padding: 0; }
  html, body { width: 945px; height: 1200px; overflow: hidden; }
  body { background: var(--backdrop); font-family: "Open Sans", sans-serif; color: var(--ink); position: relative; }

  .sheet { position: absolute; left: 54px; top: 62px; width: 832px; height: 1076px; background: var(--paper); }
  .trim { position: absolute; left: 83px; top: 88px; width: 774px; height: 1030px; border: 1px solid var(--peach-line); border-bottom: none; }

  .logo-slot { position: absolute; left: 309px; top: 120px; width: 311px; height: 70px; border: 1.5px dashed #555; text-align: center; padding-top: 11px; }
  .logo-slot__label { font-family: "Poppins", sans-serif; font-weight: 500; font-size: 17px; letter-spacing: 6px; color: var(--forest); line-height: 24px; }
  .logo-slot__name { font-family: "Poppins", sans-serif; font-size: 11px; letter-spacing: 2.5px; color: #6b6b6b; line-height: 18px; }

  .headline { position: absolute; left: 0; width: 945px; text-align: center; font-family: "Merriweather", serif; font-weight: 900; color: var(--forest); white-space: nowrap; }
  .headline--top { top: 206px; font-size: 78px; line-height: 1.1; }
  .headline--sub { top: 292px; font-size: 50px; line-height: 1.1; left: 8px; }
  .headline__accent { font-style: italic; color: var(--teal); }
  .swoosh { position: absolute; left: 592px; top: 356px; }

  .approval-badge { position: absolute; left: 192px; top: 380px; width: 548px; height: 55px; }
  .approval-badge svg { position: absolute; left: 0; top: 0; }
  .approval-badge__text { position: absolute; left: 60px; top: 0; height: 55px; line-height: 55px; color: #fff; font-size: 15.5px; white-space: nowrap; }
  .approval-badge__text b { font-weight: 700; }

  .support { position: absolute; left: 0; width: 945px; text-align: center; font-family: "Poppins", sans-serif; font-size: 13px; white-space: nowrap; }
  .support--partner { top: 448px; color: var(--ink); }
  .support--local { top: 470px; color: var(--forest); font-weight: 500; }

  .section-rule { position: absolute; left: 136px; top: 506px; width: 672px; height: 20px; }
  .section-title { position: absolute; left: 0; width: 945px; top: 505px; text-align: center; font-weight: 700; font-size: 15.5px; letter-spacing: 2.4px; color: var(--teal); white-space: nowrap; }
  .section-title span { background: var(--paper); padding: 0 8px; }

  .service { position: absolute; display: flex; align-items: center; }
  .service__icon { flex: 0 0 53px; width: 53px; height: 53px; border-radius: 50%; background: var(--mint); display: flex; align-items: center; justify-content: center; }
  .service__name { margin-left: 25px; font-size: 14px; line-height: 19px; color: var(--ink); white-space: nowrap; }
  .service--right .service__name { margin-left: 36px; }
  .service-divider { position: absolute; height: 1px; background: linear-gradient(90deg, transparent, #f5dfc0, transparent); }
  .column-divider { position: absolute; left: 468px; top: 548px; width: 1px; height: 215px; background: linear-gradient(180deg, transparent, var(--gold-soft), transparent); }

  .trust-panel { position: absolute; left: 129px; top: 802px; width: 685px; height: 105px; background: var(--mint-panel); border: 1px solid #b9c7c4; border-radius: 10px; }
  .trust-title { position: absolute; left: 0; width: 945px; top: 790px; text-align: center; font-weight: 700; font-size: 15.5px; letter-spacing: 1.4px; color: var(--forest); white-space: nowrap; }
  .trust-title span { background: var(--paper); padding: 0 10px; }
  .trust-title span::before, .trust-title span::after { content: "•"; font-size: 10px; vertical-align: middle; margin: 0 8px; }
  .trust-point { position: absolute; top: 824px; text-align: center; font-size: 13.5px; line-height: 19px; color: #3a4543; white-space: nowrap; }
  .trust-point svg { display: block; margin: 0 auto 10px; }
  .trust-sep { position: absolute; top: 826px; width: 1px; height: 66px; background: #b9c7c4; }

  .proof { position: absolute; left: 0; width: 945px; text-align: center; white-space: nowrap; }
  .proof--main { top: 918px; font-size: 24px; font-weight: 600; color: var(--forest); }
  .proof--main em { color: var(--teal); font-style: italic; }
  .proof--peers { top: 950px; font-size: 15.5px; font-style: italic; font-weight: 300; color: #4b4b4b; }

  .cta-band { position: absolute; left: 83px; top: 979px; width: 774px; height: 139px; background: var(--forest); border-radius: 0 0 14px 14px; }
  .cta-calendar { position: absolute; left: 114px; top: 998px; }
  .cta-rule { position: absolute; left: 236px; top: 998px; width: 1.5px; height: 100px; background: var(--gold); }
  .cta-title { position: absolute; left: 265px; top: 998px; font-family: "Merriweather", serif; font-weight: 700; font-size: 27px; color: #fff; white-space: nowrap; }
  .cta-title span { color: var(--gold-soft); }
  .cta-sub { position: absolute; left: 265px; top: 1038px; font-size: 16px; color: #fff; white-space: nowrap; }
  .cta-contact { position: absolute; top: 1072px; display: flex; align-items: center; color: #fff; font-size: 19px; font-weight: 600; white-space: nowrap; }
  .cta-contact svg { margin-right: 10px; flex: 0 0 27px; }
  .cta-contact--phone { left: 266px; }
  .cta-contact--email { left: 470px; font-size: 18px; }
  .cta-contact-sep { position: absolute; left: 452px; top: 1071px; width: 1.5px; height: 27px; background: #fff; }
</style>
</head>
<body>
  <div class="sheet"></div>
  <div class="trim"></div>

  <div class="logo-slot">
    <div class="logo-slot__label">YOUR LOGO HERE</div>
    <div class="logo-slot__name">Trellow Commercial Cleaning</div>
  </div>

  <h1 class="headline headline--top">THE CLEAN</h1>
  <p class="headline headline--sub">Your Residents <span class="headline__accent">notice.</span></p>
  <svg class="swoosh" width="200" height="18" viewBox="0 0 200 18"><path d="M3 15 C 60 5, 140 2, 197 8" fill="none" stroke="var(--gold)" stroke-width="3.5" stroke-linecap="round"/></svg>

  <div class="approval-badge">
    <svg width="548" height="55" viewBox="0 0 548 55">
      <polygon points="16,2 532,2 546,16 546,39 532,53 16,53 2,39 2,16" fill="var(--gold-soft)"/>
      <polygon points="18,6 530,6 541,18 541,37 530,49 18,49 7,37 7,18" fill="var(--forest)"/>
      <circle cx="33" cy="27.5" r="14" fill="none" stroke="var(--gold)" stroke-width="1.6" stroke-dasharray="3 1.5"/>
      <circle cx="33" cy="27.5" r="9" fill="none" stroke="var(--gold)" stroke-width="1.5"/>
      <path d="M28.5 27.5 l3 3 l5.5 -6" fill="none" stroke="var(--gold)" stroke-width="1.6" stroke-linecap="round"/>
    </svg>
    <p class="approval-badge__text"><b>Oakvane Residential's</b> Approved Austin Cleaning Company.</p>
  </div>

  <p class="support support--partner">Preferred Vendor Partner in Oakvane's Capitol Partner Circle.</p>
  <p class="support support--local">Texas-owned, serving Austin for 20+ years.</p>

  <svg class="section-rule" width="672" height="20" viewBox="0 0 672 20">
    <line x1="0" y1="10" x2="672" y2="10" stroke="var(--forest)" stroke-width="1"/>
    <circle cx="2.5" cy="10" r="2.5" fill="var(--forest)"/><circle cx="669.5" cy="10" r="2.5" fill="var(--forest)"/>
  </svg>
  <h2 class="section-title"><span>COMMERCIAL CLEANING SERVICES</span></h2>

  <div class="services">
    <div class="service" style="left:202px;top:535px">
      <div class="service__icon"><svg width="30" height="30" viewBox="0 0 30 30" fill="none" stroke="var(--forest)" stroke-width="1.4"><path d="M7 12h16l-2 14H9z"/><path d="M9 12c0-5 12-5 12 0"/><line x1="24" y1="3" x2="24" y2="27"/></svg></div>
      <p class="service__name">Recurring<br>Janitorial</p>
    </div>
    <div class="service" style="left:202px;top:600px">
      <div class="service__icon"><svg width="30" height="30" viewBox="0 0 30 30" fill="none" stroke="var(--forest)" stroke-width="1.4"><line x1="24" y1="3" x2="14" y2="20"/><path d="M9 20h10l2 4H7z"/><line x1="4" y1="14" x2="10" y2="14"/><line x1="3" y1="18" x2="8" y2="18"/></svg></div>
      <p class="service__name">Floor Strip Wax<br>and Buff</p>
    </div>
    <div class="service" style="left:202px;top:665px">
      <div class="service__icon"><svg width="30" height="30" viewBox="0 0 30 30" fill="none" stroke="var(--forest)" stroke-width="1.4"><path d="M5 26l4-12h16l-4 12z"/><rect x="16" y="6" width="6" height="9" rx="2"/><line x1="19" y1="3" x2="19" y2="6"/></svg></div>
      <p class="service__name">Carpet<br>Extraction</p>
    </div>
    <div class="service" style="left:202px;top:731px">
      <div class="service__icon"><svg width="30" height="30" viewBox="0 0 30 30" fill="none" stroke="var(--forest)" stroke-width="1.4"><rect x="5" y="4" width="20" height="20"/><line x1="15" y1="4" x2="15" y2="24"/><line x1="3" y1="26" x2="27" y2="26"/><line x1="8" y1="14" x2="12" y2="9"/><line x1="18" y1="14" x2="22" y2="9"/></svg></div>
      <p class="service__name">Windows<br>and Glass</p>
    </div>

    <div class="service service--right" style="left:510px;top:535px">
      <div class="service__icon"><svg width="30" height="30" viewBox="0 0 30 30" fill="none" stroke="var(--forest)" stroke-width="1.4"><path d="M4 14h22v8H4z"/><path d="M7 14v-5h16v5"/><line x1="6" y1="22" x2="6" y2="25"/><line x1="24" y1="22" x2="24" y2="25"/></svg></div>
      <p class="service__name">Upholstery<br>Care</p>
    </div>
    <div class="service service--right" style="left:510px;top:600px">
      <div class="service__icon"><svg width="30" height="30" viewBox="0 0 30 30" fill="none" stroke="var(--forest)" stroke-width="1.4"><path d="M5 8h14v5H5z"/><path d="M9 13v12h8v-8"/><line x1="19" y1="10" x2="23" y2="10"/><circle cx="26" cy="7" r="1"/><circle cx="26" cy="13" r="1"/><circle cx="27" cy="10" r="1"/></svg></div>
      <p class="service__name">Pressure<br>Washing</p>
    </div>
    <div class="service service--right" style="left:510px;top:665px">
      <div class="service__icon"><svg width="30" height="30" viewBox="0 0 30 30" fill="none" stroke="var(--forest)" stroke-width="1.4"><line x1="20" y1="3" x2="14" y2="17"/><path d="M10 16l8 3-3 7-10-2z"/><circle cx="24" cy="20" r="1.5"/><circle cx="6" cy="9" r="1"/></svg></div>
      <p class="service__name">Move-in and<br>Move-out cleans</p>
    </div>
    <div class="service service--right" style="left:510px;top:731px">
      <div class="service__icon"><svg width="30" height="30" viewBox="0 0 30 30" fill="none" stroke="var(--forest)" stroke-width="1.4"><circle cx="15" cy="15" r="4"/><line x1="5" y1="5" x2="25" y2="25"/><line x1="25" y1="5" x2="5" y2="25"/><path d="M3 8l3-5M22 3l5 3"/></svg></div>
      <p class="service__name">Damage<br>Restoration</p>
    </div>

    <div class="service-divider" style="left:178px;top:594px;width:260px"></div>
    <div class="service-divider" style="left:190px;top:659px;width:240px"></div>
    <div class="service-divider" style="left:190px;top:725px;width:220px"></div>
    <div class="service-divider" style="left:500px;top:594px;width:265px"></div>
    <div class="service-divider" style="left:510px;top:659px;width:250px"></div>
    <div class="service-divider" style="left:505px;top:725px;width:255px"></div>
    <div class="column-divider"></div>
  </div>

  <div class="trust-panel"></div>
  <h2 class="trust-title"><span>WHY PROPERTY MANAGERS TRUST TRELLOW</span></h2>

  <div class="trust-point" style="left:140px;width:115px"><svg width="30" height="30" viewBox="0 0 30 30" fill="none" stroke="var(--forest)" stroke-width="2.4" stroke-linecap="round"><path d="M25 14a11 11 0 1 1-5-9"/><path d="M10 14l4 4 11-12"/></svg>Licensed &amp;<br>Insured</div>
  <div class="trust-sep" style="left:265px"></div>
  <div class="trust-point" style="left:275px;width:140px"><svg width="30" height="30" viewBox="0 0 30 30" fill="none" stroke="var(--forest)" stroke-width="2.4" stroke-linecap="round"><path d="M25 14a11 11 0 1 1-5-9"/><path d="M10 14l4 4 11-12"/></svg>Background-<br>Checked Crews</div>
  <div class="trust-sep" style="left:421px"></div>
  <div class="trust-point" style="left:431px;width:140px"><svg width="30" height="30" viewBox="0 0 30 30" fill="none" stroke="var(--forest)" stroke-width="2.4" stroke-linecap="round"><path d="M25 14a11 11 0 1 1-5-9"/><path d="M10 14l4 4 11-12"/></svg>TrustGrid<br>Compliant</div>
  <div class="trust-sep" style="left:578px"></div>
  <div class="trust-point" style="left:585px;width:220px"><svg width="30" height="30" viewBox="0 0 30 30" fill="none" stroke="var(--forest)" stroke-width="2.4" stroke-linecap="round"><path d="M25 14a11 11 0 1 1-5-9"/><path d="M10 14l4 4 11-12"/></svg>Invoicing Through Supply<br>Nook &amp; Kelvara Systems.</div>

  <p class="proof proof--main">Already Trusted by <em>OAKVANE COMMUNITIES.</em></p>
  <p class="proof proof--peers">Ask your peers at The Brindley and The Ashford on Tulley.</p>

  <div class="cta-band"></div>
  <svg class="cta-calendar" width="100" height="100" viewBox="0 0 100 100" fill="none">
    <circle cx="50" cy="50" r="49" stroke="#e6efed" stroke-width="1.2"/>
    <rect x="23" y="25" width="54" height="52" rx="7" stroke="#d7ebe6" stroke-width="3"/>
    <line x1="23" y1="38" x2="77" y2="38" stroke="#d7ebe6" stroke-width="3"/>
    <line x1="37" y1="19" x2="37" y2="30" stroke="#d7ebe6" stroke-width="3" stroke-linecap="round"/>
    <line x1="63" y1="19" x2="63" y2="30" stroke="#d7ebe6" stroke-width="3" stroke-linecap="round"/>
    <path d="M38 56l8 8 16-17" stroke="var(--gold)" stroke-width="4" stroke-linecap="round" stroke-linejoin="round"/>
  </svg>
  <div class="cta-rule"></div>
  <p class="cta-title">Book a <span>FREE</span> Walkthrough</p>
  <p class="cta-sub">of your community. Call or email</p>
  <div class="cta-contact cta-contact--phone">
    <svg width="27" height="27" viewBox="0 0 27 27"><circle cx="13.5" cy="13.5" r="13.5" fill="var(--gold-soft)"/><path d="M9 7l3 3-2 2c1 2 3 4 5 5l2-2 3 3-2 2c-5 0-11-6-11-11z" fill="var(--forest)"/></svg>
    512-430-7156
  </div>
  <div class="cta-contact-sep"></div>
  <div class="cta-contact cta-contact--email">
    <svg width="27" height="27" viewBox="0 0 27 27"><circle cx="13.5" cy="13.5" r="13.5" fill="var(--gold-soft)"/><rect x="7" y="9" width="13" height="9" fill="none" stroke="var(--forest)" stroke-width="1.5"/><path d="M7 9l6.5 5 6.5-5" fill="none" stroke="var(--forest)" stroke-width="1.5"/></svg>
    support@trellowclean-example.com
  </div>
</body>
</html>
```